Media Training Presentation (template)

This is a 49-slide power point deck to be used in training clients to deal with the media in various settings. We need a template we can personalize for different clients. The overall color scheme should match our logo. It should look very professional, but also engaging. The word doc contains all of the text, images, and videos for each slide. Also uploaded our logo. Please match/coordinate colors of presentation to the logo colors. If you prefer, you can submit five or six slides showing the overall design and a template for each type of slide, then complete the remainder of the slides within 24 hours if chosen. (Sorry for the quick turnaround…we didn’t know we would need it this quickly!) Thanks for submitting!
Target Market(s)
Government and corporate clients

```html
<!DOCTYPE html>
<html lang="en">
<head>
<meta charset="utf-8">
<title>Media Training Presentation</title>
<link href="https://fonts.googleapis.com/css2?family=Poppins:wght@400;500;600&display=swap" rel="stylesheet">
<style>
:root{
  --blue:#0a55b0;
  --dark:#2e2e2e;
  --grey:#7f7f7f;
  --page:#eef2f8;
  --light-blue:#eef3f9;
  --light-grey:#efefef;
  --text:#222;
  --line:#8a8a8a;
}
*{margin:0;padding:0;box-sizing:border-box}
html,body{width:1200px;height:4051px;overflow:hidden;background:var(--page);font-family:'Poppins',sans-serif;color:var(--text)}
.slide{position:absolute;left:75px;width:1048px;height:588px;background:#fff;border-bottom:4px solid var(--line);box-shadow:0 6px 18px rgba(20,40,80,.08);overflow:hidden}
.slide-header{position:absolute;left:0;top:0}
.slide-title{position:absolute;left:61px;top:34px;color:#fff;font-weight:600;font-size:24px;letter-spacing:.2px}
.brand{position:absolute;left:768px;top:30px;display:flex;align-items:center;gap:14px}
.brand-square{width:34px;height:34px;border:4px solid var(--blue);border-radius:3px}
.brand-name{color:var(--blue);font-weight:400;font-size:17px;letter-spacing:2px;line-height:1.1;width:170px}
.abs{position:absolute}
/* slide 1 */
.step-frame{position:absolute;width:241px;height:241px;border:1.5px dashed #777;border-radius:4px}
.step-frame.solid{border:1.5px solid var(--blue)}
.step-box{position:absolute;width:200px;height:199px;display:flex;flex-direction:column;align-items:center;justify-content:center;gap:22px;color:#fff;font-size:13px;font-weight:500;text-align:center;line-height:1.7;box-shadow:0 4px 10px rgba(0,0,0,.25)}
.step-box.grey{background:var(--grey)} .step-box.blue{background:var(--blue)} .step-box.dark{background:var(--dark)}
/* slide 2 */
.goal-icon{position:absolute;width:106px;height:106px;border-radius:50%;background:#fff;border:9px solid var(--dark);box-shadow:0 8px 14px rgba(0,0,0,.22);display:flex;align-items:center;justify-content:center}
.goal-icon.blue{border-color:var(--blue)}
.goal-label{position:absolute;font-weight:500;font-size:18px;line-height:1.35;color:#222}
/* slide 3 */
.photo{position:absolute;left:113px;top:178px;width:485px;height:343px;border-radius:60px 0 60px 0;background:linear-gradient(120deg,#c9d3dd 0%,#9fb0c2 45%,#3a4656 100%)}
.bullets{position:absolute;left:643px;top:243px;list-style:none;font-size:18px;line-height:45px}
.bullets li::before{content:"•";margin-right:14px;font-size:14px}
/* slides 4-5 */
.rec-circle{position:absolute;border-radius:50%;display:flex;flex-direction:column;align-items:center;justify-content:center;gap:18px;text-align:center;font-size:14px;font-weight:500;line-height:1.55}
.rec-side{width:258px;height:258px}
.rec-mid{width:278px;height:278px;background:#fff}
.on .rec-side{background:var(--light-blue);color:#222}
.on .rec-mid{border:3px solid var(--blue);color:#222}
.off .rec-side{background:var(--light-grey);color:var(--blue)}
.off .rec-mid{border:3px solid #777;color:var(--blue)}
/* slide 6 */
.bg-icon{position:absolute;width:78px;height:78px;border-radius:50%;display:flex;align-items:center;justify-content:center;box-shadow:0 6px 12px rgba(0,0,0,.2);border:5px solid #fff}
.bg-icon.blue{background:var(--blue)} .bg-icon.dark{background:var(--dark)}
.bg-label{position:absolute;font-size:11px;font-weight:500;line-height:1.65;text-transform:uppercase;color:#222}
.bg-center{position:absolute;left:414px;top:231px;width:220px;height:220px;border-radius:50%;background:#fff;box-shadow:0 8px 24px rgba(10,85,176,.18);display:flex;align-items:center;justify-content:center;gap:10px}
.bg-center .brand-square{width:26px;height:26px;border-width:3px}
.bg-center .brand-name{font-size:13px;width:120px}
</style>
</head>
<body>

<!-- Slide 1 -->
<section class="slide" style="top:88px">
  <svg class="slide-header" width="1048" height="220"><path d="M0 0H828Q790 98 705 98H150Q0 98 0 205Z" fill="var(--blue)"/></svg>
  <h2 class="slide-title">WHAT IS MEDIA TRAINING?</h2>
  <div class="brand"><div class="brand-square"></div><div class="brand-name">HARLOW COMMUNICATIONS</div></div>

  <div class="step-frame" style="left:118px;top:225px"></div>
  <div class="step-box grey" style="left:137px;top:246px">
    <svg width="44" height="44" viewBox="0 0 44 44" fill="none" stroke="#fff" stroke-width="2"><rect x="4" y="6" width="28" height="22" rx="2"/><circle cx="28" cy="28" r="8"/><path d="M34 34l7 7"/></svg>
    <span>IT’S NOT NATURAL.</span>
  </div>
  <div class="step-frame solid" style="left:404px;top:225px"></div>
  <div class="step-box blue" style="left:425px;top:246px">
    <svg width="44" height="44" viewBox="0 0 44 44" fill="none" stroke="#fff" stroke-width="2"><rect x="10" y="4" width="24" height="20" rx="2"/><path d="M4 30l10-6 8 6 8-6 10 6M12 34l6 4M20 33l6 5"/></svg>
    <span>IT REQUIRES PRACTICE.</span>
  </div>
  <div class="step-frame" style="left:690px;top:225px"></div>
  <div class="step-box dark" style="left:711px;top:246px">
    <svg width="44" height="44" viewBox="0 0 44 44" fill="none" stroke="#fff" stroke-width="2"><rect x="4" y="14" width="18" height="24"/><path d="M8 20h10M8 26h10M8 32h10"/><circle cx="32" cy="12" r="5"/><path d="M24 30q8-12 16 0v8H24z"/><rect x="6" y="4" width="12" height="8"/></svg>
    <span>IT’S ABOUT DEVELOPING<br>A MINDSET.</span>
  </div>
  <svg class="abs" style="left:0;top:0" width="1048" height="588" fill="none" stroke="#666" stroke-width="1.5">
    <path d="M359 345H398"/><path d="M392 340l6 5-6 5" fill="#666"/>
    <path d="M645 345H684" stroke="var(--blue)"/><path d="M678 340l6 5-6 5" fill="var(--blue)" stroke="var(--blue)"/>
  </svg>
</section>

<!-- Slide 2 -->
<section class="slide" style="top:736px">
  <svg class="slide-header" width="1048" height="220"><path d="M0 0H828Q790 98 705 98H150Q0 98 0 205Z" fill="var(--blue)"/></svg>
  <h2 class="slide-title">GOALS</h2>
  <div class="brand"><div class="brand-square"></div><div class="brand-name">HARLOW COMMUNICATIONS</div></div>

  <svg class="abs" style="left:0;top:0" width="1048" height="588">
    <path d="M285 588A252 252 0 0 1 763 588" fill="none" stroke="#5b6fb0" stroke-width="1.5" stroke-dasharray="5 4"/>
    <circle cx="524" cy="615" r="195" fill="var(--grey)"/>
    <circle cx="285" cy="538" r="9" fill="#fff" stroke="var(--blue)" stroke-width="4"/>
    <circle cx="442" cy="378" r="9" fill="#fff" stroke="var(--dark)" stroke-width="4"/>
    <circle cx="612" cy="378" r="9" fill="#fff" stroke="var(--blue)" stroke-width="4"/>
    <circle cx="765" cy="538" r="9" fill="#fff" stroke="var(--dark)" stroke-width="4"/>
  </svg>
  <div class="brand" style="left:410px;top:495px"><div class="brand-square" style="border-color:#fff"></div><div class="brand-name" style="color:#fff;width:190px">HARLOW COMMUNICATIONS</div></div>

  <div class="goal-label" style="left:258px;top:136px;text-align:center;width:160px">Develop a<br>strategy</div>
  <div class="goal-label" style="left:679px;top:136px">Clarify<br>message</div>
  <div class="goal-label" style="left:40px;top:326px;width:176px;text-align:right">Learn how to<br>prepare</div>
  <div class="goal-label" style="left:847px;top:326px">Build a practice<br>approach</div>

  <div class="goal-icon" style="left:313px;top:219px"><svg width="40" height="40" viewBox="0 0 40 40" fill="none" stroke="#222" stroke-width="2"><path d="M6 34L30 10l4 4-24 24z"/><circle cx="12" cy="12" r="6"/><circle cx="28" cy="30" r="5"/></svg></div>
  <div class="goal-icon blue" style="left:620px;top:219px"><svg width="40" height="40" viewBox="0 0 40 40" fill="none" stroke="#222" stroke-width="2"><path d="M6 18a14 12 0 1 1 6 10l-6 6 2-8a12 12 0 0 1-2-8z"/><path d="M14 16h12M14 21h9"/></svg></div>
  <div class="goal-icon blue" style="left:134px;top:413px"><svg width="40" height="40" viewBox="0 0 40 40" fill="none" stroke="#222" stroke-width="2"><rect x="4" y="8" width="24" height="26"/><circle cx="30" cy="10" r="6"/><path d="M8 16h14M8 22h14M8 28h10"/></svg></div>
  <div class="goal-icon" style="left:810px;top:413px"><svg width="40" height="40" viewBox="0 0 40 40" fill="none" stroke="#222" stroke-width="2"><circle cx="20" cy="20" r="6"/><path d="M20 4v6M20 30v6M4 20h6M30 20h6M9 9l4 4M27 27l4 4M9 31l4-4M27 13l4-4"/><circle cx="20" cy="20" r="12"/></svg></div>
</section>

<!-- Slide 3 -->
<section class="slide" style="top:1395px">
  <svg class="slide-header" width="1048" height="220"><path d="M0 0H828Q790 98 705 98H150Q0 98 0 205Z" fill="var(--blue)"/></svg>
  <h2 class="slide-title">WHAT TO NEGOTIATE?</h2>
  <div class="brand"><div class="brand-square"></div><div class="brand-name">HARLOW COMMUNICATIONS</div></div>
  <div class="photo" role="img" aria-label="Photo of an interviewer and guest shaking hands beside a camera in a bright office"></div>
  <ul class="bullets">
    <li>Timing and location</li>
    <li>Rules of recording/broadcast</li>
    <li>Rules of translation</li>
    <li>Questions</li>
    <li>Recording (for accuracy)</li>
  </ul>
</section>

<!-- Slide 4 -->
<section class="slide on" style="top:2054px">
  <svg class="slide-header" width="1048" height="220"><path d="M0 0H828Q790 98 705 98H150Q0 98 0 205Z" fill="var(--blue)"/></svg>
  <h2 class="slide-title">ON THE RECORD</h2>
  <div class="brand"><div class="brand-square"></div><div class="brand-name">HARLOW COMMUNICATIONS</div></div>
  <div class="rec-circle rec-side" style="left:151px;top:209px">
    <svg width="54" height="54" viewBox="0 0 54 54" fill="none" stroke="var(--blue)" stroke-width="2.5"><rect x="14" y="6" width="26" height="14"/><rect x="6" y="20" width="42" height="20" rx="3"/><rect x="14" y="32" width="26" height="16"/><path d="M18 38h18M18 43h12"/></svg>
    <span>EVERYTHING FOR<br>PRINT</span>
  </div>
  <div class="rec-circle rec-side" style="left:640px;top:209px">
    <svg width="54" height="54" viewBox="0 0 54 54" fill="none" stroke="var(--blue)" stroke-width="2.5"><rect x="20" y="6" width="14" height="26" rx="7"/><path d="M14 24a13 13 0 0 0 26 0M27 37v10M20 47h14M6 20v10M10 16v18M44 16v18M48 20v10"/></svg>
    <span>ALWAYS ASSUME<br>EVERYTHING IS ON THE<br>RECORD</span>
  </div>
  <div class="rec-circle rec-mid" style="left:385px;top:199px">
    <svg width="54" height="54" viewBox="0 0 54 54" fill="none" stroke="var(--blue)" stroke-width="2.5"><circle cx="16" cy="30" r="7"/><path d="M4 48q12-14 24 0"/><path d="M30 34V24M36 34V18M42 34V12M48 34V8"/></svg>
    <span>YOUR NAME FOR<br>ATTRIBUTION</span>
  </div>
</section>

<!-- Slide 5 -->
<section class="slide off" style="top:2713px">
  <svg class="slide-header" width="1048" height="220"><path d="M0 0H828Q790 98 705 98H150Q0 98 0 205Z" fill="var(--blue)"/></svg>
  <h2 class="slide-title">OFF THE RECORD</h2>
  <div class="brand"><div class="brand-square"></div><div class="brand-name">HARLOW COMMUNICATIONS</div></div>
  <div class="rec-circle rec-side" style="left:151px;top:209px">
    <svg width="54" height="54" viewBox="0 0 54 54" fill="none" stroke="#666" stroke-width="2"><circle cx="32" cy="20" r="13"/><path d="M22 30L8 46"/><path d="M26 20h2M31 20h2M36 20h2"/></svg>
    <span>NOT FOR<br>PRINT</span>
  </div>
  <div class="rec-circle rec-side" style="left:640px;top:209px">
    <svg width="54" height="54" viewBox="0 0 54 54" fill="none" stroke="#666" stroke-width="2"><path d="M18 30V10a4 4 0 0 1 8 0v16l14 4a6 6 0 0 1 4 7l-3 11H22l-8-12a4 4 0 0 1 6-5z"/><path d="M10 14a12 12 0 0 1 24 0"/></svg>
    <span>DOESN’T MEAN<br>IT WON’T BE USED/<br>PRINTED</span>
  </div>
  <div class="rec-circle rec-mid" style="left:385px;top:199px">
    <svg width="54" height="54" viewBox="0 0 54 54" fill="none" stroke="#666" stroke-width="3"><circle cx="27" cy="27" r="20"/><path d="M13 13l28 28"/></svg>
    <span>NOT FOR<br>ATTRIBUTION</span>
  </div>
</section>

<!-- Slide 6 -->
<section class="slide" style="top:3372px">
  <svg class="slide-header" width="1048" height="220"><path d="M0 0H828Q790 98 705 98H150Q0 98 0 205Z" fill="var(--blue)"/></svg>
  <h2 class="slide-title">ON BACKGROUND</h2>
  <div class="brand"><div class="brand-square"></div><div class="brand-name">HARLOW COMMUNICATIONS</div></div>
  <svg class="abs" style="left:0;top:0" width="1048" height="588" fill="none" stroke-width="1.5">
    <circle cx="524" cy="341" r="134" stroke="#bbb"/>
    <path d="M330 242H372L410 273" stroke="var(--blue)"/>
    <path d="M330 445H372L410 409" stroke="var(--dark)"/>
    <path d="M718 242H680L638 273" stroke="var(--dark)"/>
    <path d="M718 445H680L638 409" stroke="var(--blue)"/>
    <circle cx="410" cy="273" r="5" fill="#fff" stroke="var(--blue)" stroke-width="2"/>
    <circle cx="410" cy="409" r="5" fill="#fff" stroke="var(--dark)" stroke-width="2"/>
    <circle cx="638" cy="273" r="5" fill="#fff" stroke="var(--dark)" stroke-width="2"/>
    <circle cx="638" cy="409" r="5" fill="#fff" stroke="var(--blue)" stroke-width="2"/>
  </svg>
  <div class="bg-center"><div class="brand-square"></div><div class="brand-name">HARLOW COMMUNICATIONS</div></div>

  <div class="bg-icon blue" style="left:251px;top:203px"><svg width="32" height="32" viewBox="0 0 32 32" fill="none" stroke="#fff" stroke-width="2"><path d="M2 12l14-6 14 6-14 6z"/><path d="M8 15v6q8 5 16 0v-6"/><rect x="6" y="24" width="20" height="5"/></svg></div>
  <div class="bg-icon dark" style="left:251px;top:406px"><svg width="32" height="32" viewBox="0 0 32 32" fill="none" stroke="#fff" stroke-width="2"><path d="M10 24a10 10 0 1 1 12 0v4H10z"/><path d="M12 30h8M16 10v8"/></svg></div>
  <div class="bg-icon dark" style="left:719px;top:203px"><svg width="32" height="32" viewBox="0 0 32 32" fill="none" stroke="#fff" stroke-width="2"><circle cx="10" cy="12" r="4"/><circle cx="22" cy="12" r="4"/><path d="M3 28q7-10 14 0M15 28q7-10 14 0"/><rect x="12" y="2" width="8" height="5"/></svg></div>
  <div class="bg-icon blue" style="left:719px;top:406px"><svg width="32" height="32" viewBox="0 0 32 32" fill="none" stroke="#fff" stroke-width="2"><rect x="9" y="4" width="14" height="8"/><rect x="4" y="12" width="24" height="11" rx="2"/><rect x="9" y="19" width="14" height="9"/></svg></div>

  <div class="bg-label" style="left:80px;top:233px;width:152px;text-align:right">Education</div>
  <div class="bg-label" style="left:80px;top:426px;width:152px;text-align:right">Can be used with<br>attribution</div>
  <div class="bg-label" style="left:818px;top:224px;width:150px">Attribution to be<br>negotiated</div>
  <div class="bg-label" style="left:818px;top:436px;width:150px">Context for print</div>
</section>

</body>
</html>
```